Supplement Label Design for “Kept 2 Thrive Core” – Premium Bilingual Supplement

Kept 2 Thrive is a premium, individually crafted supplement brand specializing in targeted solutions for specific health issues.
We are launching our first product: Kept 2 Thrive Core — a high-quality blend focused on stomach and digestive health.
Primary goals:
• Reduce symptoms caused by Helicobacter pylori (acidity after meals, stomach pain and discomfort)
• Support repair of the gut lining
• Strengthen the local immune system in the digestive tract
Label Requirements:
• Premium, elegant, and modern design (high-end supplement feel)
• Dominant yellow / golden color scheme for this Gut blend (future blends will have different signature colors, e.g. red for Pulse blend)
• Include a stylized, positive illustration of a healthy stomach on the label
• Fully bilingual — English and Bulgarian if possible (both languages must be clearly visible and well balanced)
• Logo is already uploaded
• Must feel trustworthy, clean, and professional
We need both front and back label designs suitable for a standard supplement bottle.

Target Market(s)

The target is health-conscious individuals, particularly my personal patients who suffer from stomach issues, H. pylori related symptoms, and digestive discomfort. People looking for premium, science-oriented natural supplements.

Industry/Entity Type

Functional medicine

Font styles to use
Sans Serif

Colors
FFC000
F8CF3A
FAE287
FDF2CF
FEFAEE

Requirements
Must have
• • Premium and luxurious look • Dominant yellow/golden color palette • Stylized healthy stomach illustration • Bilingual (English + Bulgarian) • Clean, minimalist yet elegant design • Professional and trustworthy appearance • Include the “Kept 2 Thrive” logo
Nice to have
• • Subtle visual indication of positive effect on the stomach/gut • Elegant iconography or subtle patterns related to health and nature • Easy-to-read hierarchy for important information • Modern minimalist style with premium finishing feel
Should not have
• Cheap or generic look • Overly cartoonish or childish stomach drawing • Too much clutter or overcrowded desig

```html
<!DOCTYPE html>
<html lang="en">
<head>
<meta charset="utf-8">
<title>Kept 2 Thrive Core – Label</title>
<link href="https://fonts.googleapis.com/css2?family=Cinzel:wght@600&family=Montserrat:wght@400;500;600;700;800&display=swap" rel="stylesheet">
<style>
  :root {
    --backdrop: #FDD866;
    --label: #F3F0E7;
    --gold: #C9A45C;
    --gold-dark: #B58E45;
    --gold-light: #E4CB96;
    --ink: #1F1F1F;
    --ink-soft: #3A3A3A;
    --rule: #2B2B2B;
  }
  * { margin: 0; padding: 0; box-sizing: border-box; }
  html, body { width: 858px; height: 1200px; overflow: hidden; }
  body {
    background: var(--backdrop);
    font-family: "Montserrat", sans-serif;
    color: var(--ink);
    position: relative;
  }
  .label {
    position: absolute;
    left: 20px; top: 284px;
    width: 818px; height: 632px;
    background: var(--label);
  }

  /* front panel */
  .front { position: absolute; left: 0; top: 0; width: 410px; height: 632px; }
  .brand {
    position: absolute; top: 56px; left: 0; width: 410px;
    display: flex; justify-content: center; align-items: center; gap: 8px;
    font-family: "Montserrat", sans-serif; font-weight: 500;
    font-size: 24px; letter-spacing: 0.5px; color: var(--gold);
  }
  .brand-dot { width: 9px; height: 9px; border-radius: 50%; background: var(--gold); }
  .product-name {
    position: absolute; top: 122px; left: 0; width: 410px; text-align: center;
    font-family: "Cinzel", serif; font-weight: 600; font-size: 104px; line-height: 1;
    background: linear-gradient(90deg, var(--gold-dark), var(--gold-light) 55%, var(--gold) 100%);
    -webkit-background-clip: text; background-clip: text; color: transparent;
  }
  .subtitle {
    position: absolute; top: 238px; left: 0; width: 410px; text-align: center;
    font-weight: 700; font-size: 17px; letter-spacing: 0.2px; color: var(--ink);
  }
  .stomach-art {
    position: absolute; left: 100px; top: 287px; width: 210px; height: 170px;
    border-radius: 48% 52% 45% 55% / 50% 45% 55% 50%;
    background: radial-gradient(ellipse at 55% 45%, #F0E3C4 0%, #DCC08A 60%, #F3F0E7 100%);
  }
  .claim {
    position: absolute; top: 481px; left: 82px; width: 244px; text-align: center;
    font-weight: 700; font-size: 15.5px; color: var(--ink);
    padding-bottom: 5px; border-bottom: 1.2px solid var(--rule);
  }
  .claim-bg {
    position: absolute; top: 516px; left: 60px; width: 290px; text-align: center;
    font-size: 11.5px; line-height: 1.35; color: var(--ink-soft); letter-spacing: 0.2px;
  }
  .badge {
    position: absolute; top: 575px; left: 83px; width: 244px; height: 22px;
    border-radius: 11px; background: var(--gold);
    color: #fff; font-weight: 700; font-size: 9.6px; letter-spacing: 0.3px;
    display: flex; align-items: center; justify-content: center;
  }

  /* back panel */
  .back-col {
    position: absolute; top: 56px; width: 170px;
    font-size: 5.4px; line-height: 1.3; color: var(--ink);
  }
  .back-col.en { left: 438px; }
  .back-col.bg { left: 622px; }
  .col-divider {
    position: absolute; left: 612px; top: 54px; width: 0.8px; height: 540px;
    background: var(--rule);
  }
  .section-title { color: var(--gold); font-weight: 600; font-size: 6px; margin-bottom: 4px; }
  .back-col p { text-align: justify; margin-bottom: 7px; }
  .hl { color: var(--gold); font-weight: 600; }
  .block { position: absolute; left: 0; width: 170px; }
  .rule { position: absolute; left: 0; width: 170px; height: 0.8px; background: var(--rule); }

  .components {
    width: 170px; border: 0.8px solid var(--rule); border-radius: 5px; overflow: hidden;
    border-collapse: separate; border-spacing: 0; font-size: 5.4px;
  }
  .components th {
    background: var(--gold); color: #fff; font-weight: 600; text-align: left;
    padding: 3px 5px; font-size: 5.4px;
  }
  .components td { padding: 1px 5px; vertical-align: top; }
  .components td + td { border-left: 0.8px solid var(--rule); white-space: nowrap; }
  .components tbody tr:first-child td { padding-top: 4px; }
  .components tbody tr:last-child td { padding-bottom: 4px; }
</style>
</head>
<body>
<main class="label">
  <section class="front">
    <div class="brand"><span>Kept 2</span><span class="brand-dot"></span><span>Thrive</span></div>
    <h1 class="product-name">CORE</h1>
    <p class="subtitle">FUNCTIONAL SUPPORT BLEND</p>
    <div class="stomach-art" role="img" aria-label="Gold engraved illustration of a healthy stomach"></div>
    <p class="claim">DIGESTIVE HEALTH &amp; REPAIR</p>
    <p class="claim-bg">ПОДКРЕПА ЗА ХРАНОСМИЛАНЕТО И<br>ВЪЗСТАНОВЯВАНЕ</p>
    <div class="badge">DOCTOR FORMULATED-60 VEG CAPSULES</div>
  </section>

  <div class="col-divider"></div>

  <section class="back-col en" lang="en">
    <div class="block" style="top:0">
      <p class="section-title">Kept 2 Thrive Core</p>
      <p>Food supplement with vegetable extracts of Licorice, Red elm, Althaea, Aloe vera, with Mastics of Chios, N-acetylcysteine and Lactoferrin.</p>
      <p class="section-title">Capsules of 735 mg &nbsp; Net weight: 102,9 g</p>
      <p class="section-title">COMPOSITION:</p>
      <p>Chios mastica (Pistacia lentinus L. gum-resin; carrier: corn maltodextrin); capsule [hidroxypropylmethylcellulose]; licorice deglycyrrhizinated d.e. 1:4 (Glycyrrhiza glabra L. radix; carrier: corn maltodextrin); aloe vera gel 200:1 (Aloe vera (L.) Burm.f., gelum sine cute); N-acetylcysteine; Red elm d.e.10:1 (Ulmus rubra Muhl. cortex); Althaea d.e. 1:4 (Althaea officinalis L. radix; carrier: corn maltodextrin); Lactoferrin 95% (milk and product thereof - including lactose); corn maltodextrin; anticaking agent: silicon dioxide.</p>
    </div>
    <div class="block" style="top:170px">
      <table class="components">
        <thead><tr><th>COMPONENTS</th><th>Per cps</th><th>Per 3 cps</th></tr></thead>
        <tbody>
          <tr><td>Chios Mastica</td><td>320 mg</td><td>960 mg</td></tr>
          <tr><td>Licorice deglycyrrhizinated d.e</td><td>80 mg</td><td>240 mg</td></tr>
          <tr><td>Aloe vera d.e.</td><td>50 mg</td><td>150 mg</td></tr>
          <tr><td>N-acetylcysteine</td><td>40 mg</td><td>120 mg</td></tr>
          <tr><td>Red elm d.e.</td><td>40 mg</td><td>120 mg</td></tr>
          <tr><td>Althaea d.e.</td><td>40 mg</td><td>120 mg</td></tr>
          <tr><td>Lactoferrin</td><td>30 mg</td><td>90 mg</td></tr>
        </tbody>
      </table>
    </div>
    <div class="rule" style="top:276px"></div>
    <div class="block" style="top:288px">
      <p class="section-title">PHYSIOLOGICAL VALUES:</p>
      <p>Pistacia lentiscus and Licorice supports digestive system function</p>
      <p><span class="hl">RECOMMENDED DAILY DOSAGE:</span> It is recommended to take up to three capsules per day.</p>
      <p><span class="hl">STORAGE CONDITIONS:</span> Store in a cool (&lt;25°C), dry place away from sources of light and heat. RECOMMENDATIONS: Keep out of reach of children. Food supplements are not intended as a substitute for a varied and balanced diet and a healthy lifestyle. Do not exceed the recommended daily dose. The expiration date refers to the product in its intact packaging and stored correctly. SPECIAL INSTRUCTIONS: Do not give to children under 12 years of age. Consult your doctor if you are pregnant or breastfeeding. Do not use for extended periods without consulting your doctor.</p>
    </div>
    <div class="rule" style="top:434px"></div>
    <div class="block" style="top:446px">
      <p class="section-title" style="margin-bottom:1px">MANUFACTURER:</p>
      <p>LVR FARMACEUTICA – via Ombrone 9, 52025 Montevarchi (AR) – Italy</p>
      <p class="section-title" style="margin-bottom:1px">DISTRIBUTOR:</p>
      <p style="margin-bottom:0">NRD TRADING – registered company address and phone</p>
      <p>Lotto: &nbsp;&nbsp;&nbsp;&nbsp;&nbsp;&nbsp;&nbsp;&nbsp;&nbsp;&nbsp;&nbsp;&nbsp;&nbsp;&nbsp;&nbsp;&nbsp;&nbsp;&nbsp;&nbsp;&nbsp; Scadenza:</p>
    </div>
  </section>

  <section class="back-col bg" lang="bg">
    <div class="block" style="top:0">
      <p class="section-title">КЕПТ ТУ ТРАЙВ КОР</p>
      <p>Хранителна добавка с растителни екстракти от Женско биле, Червен бряст, Алтея, Алое вера, с Мастика от Хиос, N-ацетилцистеин и Лактоферин.</p>
      <p class="section-title">капсули от 735 мг / &nbsp;Нетно тегло: 102,9 г</p>
      <p class="section-title">СЪСТАВ:</p>
      <p>Мастика от Хиос (Pistacia lentinus L. гумена смола; носител: царевичен малтодекстрин); капсула [хидроксипропилметилцелулоза]; деглицирizирано женско биле 1:4 (Glycyrrhiza glabra L. корен; царевичен малтодекстрин); гел от алое вера 200:1 (Aloe vera (L.) Burm.f. gelum sine cute); N-ацетилцистеин; червен бряст 10:1 (Ulmus rubra Muhl. кора); алтея 1:4 (Althaea officinalis L. корен; царевичен малтодекстрин); Лактоферин 95% (мляко и продукти от него - включително лактоза); царевичен малтодекстрин; агент против слепване: силициев диоксид.</p>
    </div>
    <div class="block" style="top:170px">
      <table class="components">
        <thead><tr><th>СЪСТАВКИ</th><th>За 1 капсула</th><th>За 3 капсули</th></tr></thead>
        <tbody>
          <tr><td>Мастика от Хиос</td><td>320 мг</td><td>960 мг</td></tr>
          <tr><td>Женско биле с.е.</td><td>80 мг</td><td>240 мг</td></tr>
          <tr><td>Алое вера с.е.</td><td>50 мг</td><td>150 мг</td></tr>
          <tr><td>N-ацетилцистеин</td><td>40 мг</td><td>120 мг</td></tr>
          <tr><td>Червен бряст с.е.</td><td>40 мг</td><td>120 мг</td></tr>
          <tr><td>Алтея с.е.</td><td>40 мг</td><td>120 мг</td></tr>
          <tr><td>Лактоферин</td><td>30 мг</td><td>90 мг</td></tr>
        </tbody>
      </table>
    </div>
    <div class="rule" style="top:276px"></div>
    <div class="block" style="top:288px">
      <p class="section-title">PHYSIOLOGICAL VALUES:</p>
      <p>Pistacia lentiscus and Licorice supports digestive system function</p>
      <p><span class="hl">RECOMMENDED DAILY DOSAGE:</span> It is recommended to take up to three capsules per day.</p>
      <p><span class="hl">STORAGE CONDITIONS:</span> Store in a cool (&lt;25°C), dry place away from sources of light and heat. RECOMMENDATIONS: Keep out of reach of children. Food supplements are not intended as a substitute for a varied and balanced diet and a healthy lifestyle. Do not exceed the recommended daily dose. The expiration date refers to the product in its intact packaging and stored correctly. SPECIAL INSTRUCTIONS: Do not give to children under 12 years of age. Consult your doctor if you are pregnant or breastfeeding. Do not use for extended periods without consulting your doctor.</p>
    </div>
    <div class="rule" style="top:434px"></div>
    <div class="block" style="top:446px">
      <p class="section-title" style="margin-bottom:1px">ПРОИЗВОДИТЕЛ:</p>
      <p>ЛВР Фармачеутика – виа Омброне 9, 52025 Montevarchi (AR)</p>
      <p class="section-title" style="margin-bottom:1px">ДИСТРИБУТОР:</p>
      <p>НРД Трейдинг – официален адрес на фирмата и телефон</p>
      <p style="margin-bottom:0">Регистрационен номер: Дата на вписване:</p>
      <p>Партида &nbsp;&nbsp;&nbsp;&nbsp;&nbsp;&nbsp;&nbsp;&nbsp;&nbsp;&nbsp;&nbsp;&nbsp; Срок на годност:</p>
    </div>
  </section>
</main>
</body>
</html>
```